Chilli Sauce - Label for Chilli Sauce bottle

I want a design for my chilli sauce label. I have included an example from an existing product. The key features of a successful design are as follows:
1. It shows the supplier: Brisk Meadow Condiments or Brisk Meadow if a shorter label fits better.
2. We need to have space for the ingredients. We will add these after.
3. Simple is good, refer attached. It doesn't need to be a design/logo, but a great design would be wonderful.
4. Some ideas. Brisk Meadow at the top of the label. Chilli Sauce in the middle of the label. Made with local ingredients (optional). Contains chilli - believe it or not (optional or similar wording)

```html
<!DOCTYPE html>
<html lang="en">
<head>
<meta charset="utf-8">
<title>Brisk Meadow Chilli Sauce Label</title>
<link rel="stylesheet" href="https://fonts.googleapis.com/css2?family=Fredoka:wght@400;600;700&family=Roboto:wght@500&display=swap">
<style>
  :root {
    --canvas-bg: #ffffff;
    --label-edge: #f5bea5;
    --label-mid: #ffffff;
    --ink-dark: #383838;
    --chilli-red: #b8391a;
    --warning-red: #e3141b;
  }
  * { margin: 0; padding: 0; box-sizing: border-box; }
  html, body {
    width: 1200px;
    height: 1000px;
    overflow: hidden;
    background: var(--canvas-bg);
  }
  .canvas {
    position: relative;
    width: 1200px;
    height: 1000px;
  }
  .label {
    position: absolute;
    left: 314px;
    top: 79px;
    width: 572px;
    height: 842px;
    background: linear-gradient(90deg,
      var(--label-edge) 0%,
      var(--label-mid) 17%,
      var(--label-mid) 83%,
      var(--label-edge) 100%);
    box-shadow: 0 3px 8px rgba(0,0,0,0.18);
    font-family: "Fredoka", sans-serif;
    text-align: center;
  }
  .label > * {
    position: absolute;
    left: 0;
    width: 100%;
  }
  .brand-name {
    top: 62px;
    font-weight: 600;
    font-size: 52px;
    line-height: 60px;
    color: var(--ink-dark);
  }
  .product-title {
    top: 218px;
    color: var(--chilli-red);
    font-weight: 700;
  }
  .product-title span { display: block; }
  .title-chilli {
    font-size: 104px;
    line-height: 108px;
  }
  .title-sauce {
    font-size: 128px;
    line-height: 132px;
  }
  .tagline {
    top: 496px;
    font-weight: 600;
    font-size: 36px;
    line-height: 42px;
    color: var(--ink-dark);
  }
  .warning {
    top: 690px;
    color: var(--warning-red);
  }
  .warning-lead {
    display: block;
    font-weight: 400;
    font-size: 32px;
    line-height: 36px;
  }
  .warning-punch {
    display: block;
    font-weight: 600;
    font-size: 36px;
    line-height: 40px;
  }
  .volume {
    top: 782px;
    font-family: "Roboto", sans-serif;
    font-weight: 500;
    font-size: 22px;
    line-height: 26px;
    letter-spacing: 2px;
    color: var(--ink-dark);
  }
</style>
</head>
<body>
<main class="canvas">
  <section class="label">
    <p class="brand-name">Brisk Meadow</p>
    <h1 class="product-title">
      <span class="title-chilli">Chilli</span>
      <span class="title-sauce">Sauce</span>
    </h1>
    <p class="tagline">Made With<br>Local Ingredients</p>
    <p class="warning">
      <span class="warning-lead">Contains Chilli-</span>
      <span class="warning-punch">Believe It or Not</span>
    </p>
    <p class="volume">150ml/5.07oz</p>
  </section>
</main>
</body>
</html>
```